Water Filtration Company needs a business card design using our existing logo/colours!

We design and manufacture and export specialised water filtration equipment. Our equipment will take unclean dirty water and filters to safe clean drinkable water.
We would like to see designs using our existing logo and colours (see attached "Palette") that represents clean safe drinking water (fresh, clean designs but still professional and modern). Our customers are other businesses who supply water filtration equipment, governments, and private individuals.
BUSINESS CARD DETAILS (Common details):
Tel: + 61 7 55 419 276
www: brindlepeak.com.au
Address: 3/47 Cordwell Parade
Marlow Flats NSW 2593 Australia
(please include the word Australia as we are an international company)
Must include: COMMERCIAL WATER FILTRATION EQUIPMENT
NAME NO 1:
Owen Pritch
General Manager
Mobile: +61 427 38 91 04
Email: owen@brindlepeak.com.au
NAME NO. 2:
Gina Rosk
Business Manager
Mobile: +61 409 572 148
Email: gina@brindlepeak.com.au
Must Have:
1) PRINT READY IN .AI & .PDF FORMATS
2) Also saved in file format .ai (Adobe Illustrator - compatible with CS4)
3) Use existing LOGO & COLOURS: Please use our logo (see attached file)
4) FONTS: we have used Avenir & Helvetica in the past but are open to other font types for the address etc.
Thank you!

```html
<!DOCTYPE html>
<html lang="en">
<head>
<meta charset="utf-8">
<title>Brindle Peak – Business Card</title>
<link href="https://fonts.googleapis.com/css2?family=Arimo:wght@400;700&display=swap" rel="stylesheet">
<style>
  :root {
    --backdrop: #2e2e2e;
    --teal-light: #35b8c8;
    --teal-mid: #0d8fae;
    --teal-deep: #00608a;
    --ink-teal: #1a9fbf;
    --ink-logo: #0b6f94;
    --ink-dark: #1f3f55;
    --paper: #ffffff;
  }
  * { margin: 0; padding: 0; box-sizing: border-box; }
  html, body {
    width: 1200px;
    height: 848px;
    overflow: hidden;
    background: var(--backdrop);
    font-family: "Arimo", Helvetica, Arial, sans-serif;
  }
  .stage {
    position: relative;
    width: 1200px;
    height: 848px;
  }
  .card {
    position: absolute;
    width: 572px;
    overflow: hidden;
  }
  .card--front {
    left: 290px;
    top: 71px;
    height: 324px;
    background: linear-gradient(90deg, var(--teal-light) 0%, var(--teal-mid) 45%, var(--teal-deep) 100%);
  }
  .card--back {
    left: 297px;
    top: 435px;
    height: 330px;
    background: var(--paper);
  }
  .wordmark {
    position: absolute;
    display: flex;
    align-items: center;
    gap: 8px;
    font-weight: 700;
    letter-spacing: -0.5px;
    line-height: 1;
    white-space: nowrap;
  }
  .wordmark__dot {
    border-radius: 50%;
    flex: none;
  }
  .card--front .wordmark {
    left: 48px;
    top: 212px;
    font-size: 42px;
    color: var(--paper);
  }
  .card--front .wordmark__dot {
    width: 16px;
    height: 16px;
    background: var(--paper);
  }
  .tagline {
    position: absolute;
    left: 48px;
    top: 266px;
    font-size: 11px;
    font-weight: 700;
    letter-spacing: 1.2px;
    color: var(--paper);
    white-space: nowrap;
  }
  .card--back .wordmark {
    left: 43px;
    top: 52px;
    font-size: 26px;
    color: var(--ink-logo);
  }
  .card--back .wordmark__dot {
    width: 11px;
    height: 11px;
    background: var(--ink-logo);
  }
  .contact {
    position: absolute;
    left: 42px;
    top: 158px;
    list-style: none;
    font-size: 12px;
    line-height: 14px;
    color: var(--ink-teal);
  }
  .contact__item {
    display: flex;
    align-items: flex-start;
    gap: 7px;
    margin-bottom: 3px;
  }
  .contact__icon {
    width: 13px;
    height: 14px;
    flex: none;
    fill: var(--ink-teal);
  }
  .person {
    position: absolute;
    left: 340px;
    width: 200px;
    top: 233px;
    text-align: center;
  }
  .person__name {
    font-size: 22px;
    font-weight: 400;
    color: var(--ink-teal);
    line-height: 1.1;
  }
  .person__role {
    font-size: 12px;
    color: var(--ink-dark);
    margin-top: 2px;
  }
  .band {
    position: absolute;
    left: 0;
    bottom: 0;
    width: 100%;
    height: 38px;
    background: linear-gradient(90deg, var(--teal-light) 0%, var(--teal-mid) 40%, var(--teal-deep) 100%);
  }
</style>
</head>
<body>
<main class="stage">

  <section class="card card--front" aria-label="Card front">
    <div class="wordmark"><span class="wordmark__dot"></span>brindle peak</div>
    <p class="tagline">COMMERCIAL WATER FILTRATION EQUIPMENT</p>
  </section>

  <section class="card card--back" aria-label="Card back">
    <div class="wordmark"><span class="wordmark__dot"></span>brindle peak</div>

    <ul class="contact">
      <li class="contact__item">
        <svg class="contact__icon" viewBox="0 0 14 14" aria-hidden="true">
          <rect x="0.5" y="3" width="13" height="9" rx="1"/>
          <path d="M1 3.5 L7 8 L13 3.5" fill="none" stroke="#fff" stroke-width="1.2"/>
        </svg>
        <span>owen@brindlepeak.com.au</span>
      </li>
      <li class="contact__item">
        <svg class="contact__icon" viewBox="0 0 14 14" aria-hidden="true">
          <rect x="3.5" y="0.5" width="7" height="13" rx="1.2"/>
          <rect x="4.8" y="2.2" width="4.4" height="5" fill="#fff"/>
        </svg>
        <span>+61 427 38 91 04</span>
      </li>
      <li class="contact__item">
        <svg class="contact__icon" viewBox="0 0 14 14" aria-hidden="true">
          <path d="M3.2 1 L5.4 1 L6.3 4.2 L4.8 5.3 C5.6 7 7 8.4 8.7 9.2 L9.8 7.7 L13 8.6 L13 10.8 C13 12 12 13 10.8 13 C5.4 13 1 8.6 1 3.2 C1 2 2 1 3.2 1 Z"/>
        </svg>
        <span>+ 61 7 55 419 276</span>
      </li>
      <li class="contact__item">
        <svg class="contact__icon" viewBox="0 0 14 14" aria-hidden="true">
          <circle cx="7" cy="7" r="6.3"/>
          <path d="M1 7 H13 M7 0.8 C4.2 4 4.2 10 7 13.2 M7 0.8 C9.8 4 9.8 10 7 13.2" fill="none" stroke="#fff" stroke-width="0.9"/>
        </svg>
        <span>brindlepeak.com.au</span>
      </li>
      <li class="contact__item">
        <svg class="contact__icon" viewBox="0 0 14 14" aria-hidden="true">
          <path d="M7 0.5 A4.6 4.6 0 0 1 11.6 5.1 C11.6 8.4 7 13.5 7 13.5 C7 13.5 2.4 8.4 2.4 5.1 A4.6 4.6 0 0 1 7 0.5 Z"/>
          <circle cx="7" cy="5" r="1.7" fill="#fff"/>
        </svg>
        <span>3/47 Cordwell Parade<br>Marlow Flats NSW<br>2593 Australia</span>
      </li>
    </ul>

    <div class="person">
      <p class="person__name">Owen Pritch</p>
      <p class="person__role">General Manager</p>
    </div>

    <div class="band"></div>
  </section>

</main>
</body>
</html>
```